Flyer for Aluminium recycling business

We are a startup aluminium recycling business. We don’t have a logo yet. I’ve attached a flyer created by one of our sales people but it’s a bit average and we need something a bit more modern and slick. You have creative license to completely change everything - as long as the information being communicated is the same.

Target Market(s)

Hospitality, Hotels, Apartment blocks, malls etcs

Industry/Entity Type

Aluminium recycling

Requirements
Must have
• the wording
Nice to have
• you have free license on design aspect

```html
<!DOCTYPE html>
<html lang="en">
<head>
<meta charset="utf-8">
<title>Circle Metal – Aluminium Recycling Flyer</title>
<link rel="stylesheet" href="https://fonts.googleapis.com/css2?family=Poppins:wght@500;600;700&family=Syne:wght@700;800&display=swap">
<style>
  :root {
    --navy: #0b2170;
    --navy-deep: #08185a;
    --charcoal: #24262b;
    --paper: #f7f7f8;
    --white: #ffffff;
    --backdrop: #e6e6e8;
    --rule: rgba(255,255,255,0.55);
  }
  * { box-sizing: border-box; margin: 0; padding: 0; }
  html, body {
    width: 1200px; height: 960px; overflow: hidden;
    background: var(--backdrop);
    font-family: "Poppins", sans-serif;
  }
  .flyer {
    position: absolute; left: 275px; top: 20px;
    width: 650px; height: 920px;
    background: var(--paper);
    overflow: hidden;
    box-shadow: 0 6px 24px rgba(0,0,0,0.12);
  }
  .hero-photo {
    position: absolute; left: 0; top: 0; width: 650px; height: 510px;
    background: linear-gradient(170deg, #1f2126 0%, #2f3238 30%, #6f7a84 55%, #a9a59a 72%, #3a3d44 100%);
  }
  .brand {
    position: absolute; top: 50px; left: 0; width: 100%;
    display: flex; justify-content: center; align-items: center; gap: 14px;
    color: var(--white);
    font-family: "Syne", sans-serif; font-weight: 800;
    font-size: 24px; letter-spacing: 2px; line-height: 1;
  }
  .brand-dot { width: 34px; height: 34px; border-radius: 50%; background: var(--white); }
  .headline-band {
    position: absolute; left: 0; top: 370px; width: 650px; height: 140px;
    background: linear-gradient(180deg, rgba(36,38,43,0.55), rgba(36,38,43,0.92));
  }
  .headline {
    position: absolute; left: 42px; top: 398px;
    color: var(--white);
    font-family: "Syne", sans-serif; font-weight: 800;
    font-size: 21px; line-height: 1.3; letter-spacing: 0.5px;
    white-space: nowrap;
  }
  .tagline {
    position: absolute; left: 42px; top: 526px; width: 580px;
    color: var(--navy); font-weight: 700; font-size: 19px; line-height: 1.25;
  }
  .steps {
    position: absolute; left: 42px; top: 596px; width: 345px;
    background: var(--navy); border-radius: 18px;
    color: var(--white); padding: 34px 20px 12px 20px;
  }
  .steps-tab {
    position: absolute; left: 0; top: -10px;
    background: var(--paper); color: var(--navy);
    font-weight: 700; font-size: 15px; line-height: 1.2;
    padding: 8px 28px 6px 22px; border-radius: 0 0 16px 0;
  }
  .steps ul, .materials ul { list-style: none; }
  .steps li {
    position: relative; padding: 3px 0 3px 16px;
    font-size: 10.5px; font-weight: 500; line-height: 1.25;
    border-bottom: 1px solid var(--rule);
  }
  .steps li:last-child { border-bottom: none; }
  .steps li::before, .materials li::before {
    content: ""; position: absolute; left: 0; top: 8px;
    width: 6px; height: 6px; border-radius: 50%; background: currentColor;
  }
  .materials {
    position: absolute; left: 408px; top: 596px; width: 220px;
    color: var(--navy);
  }
  .materials h2 { font-size: 15px; font-weight: 700; line-height: 1.2; margin-bottom: 8px; }
  .materials li {
    position: relative; padding-left: 14px; margin-bottom: 8px;
    font-size: 11px; font-weight: 600; line-height: 1.3;
  }
  .contact-bar {
    position: absolute; left: 0; bottom: 0; width: 650px; height: 78px;
    background: var(--navy);
    display: flex; align-items: center; justify-content: center; gap: 50px;
    color: var(--white); font-weight: 600; font-size: 17px;
  }
  .contact-item { display: flex; align-items: center; gap: 12px; }
  .contact-icon { width: 30px; height: 30px; }
</style>
</head>
<body>
  <main class="flyer">
    <div class="hero-photo" role="img" aria-label="Photograph of a metal recycling bin filled with crushed aluminium drink cans"></div>

    <div class="brand"><span class="brand-dot"></span><span>CIRCLE METAL</span></div>

    <div class="headline-band"></div>
    <h1 class="headline">PLAYING THE FAIR<br>ALUMINIUM RECYCLING GAME<br>FOR GOOD</h1>

    <p class="tagline">Our partnership with you is based on common sense, mutual gain and a better tomorrow</p>

    <section class="steps">
      <div class="steps-tab">IT'S SIMPLE:</div>
      <ul>
        <li>We bring you a free bin.</li>
        <li>You throw all and any aluminium waste into the bin – no need to super-clean it. Try to compact / squash the aluminium as much as possible.</li>
        <li>We collect the bin at no charge</li>
        <li>We turn the aluminium waste into a desirable resource.</li>
        <li>We pay you for however much of that resource your waste has generated – and give you a report on that, so you can see how good you are.</li>
      </ul>
    </section>

    <section class="materials">
      <h2>Examples of<br>what we can take:</h2>
      <ul>
        <li>Used beverage cans – any.</li>
        <li>Tinfoil – scrunched, crusty, burned or dirty.</li>
        <li>Disposable BBQ roasting trays.</li>
        <li>Aluminium takeaway containers.</li>
        <li>Wine bottle screw tops (and collars – if you can get them off).</li>
        <li>Tear-off can lids.</li>
      </ul>
    </section>

    <footer class="contact-bar">
      <div class="contact-item">
        <svg class="contact-icon" viewBox="0 0 30 30" aria-hidden="true">
          <circle cx="15" cy="15" r="15" fill="#ffffff"/>
          <path d="M10 8.5c.6-.6 1.5-.5 2 .1l1.6 2.1c.4.6.3 1.3-.2 1.8l-.9.8c.7 1.6 2 2.9 3.6 3.6l.8-.9c.5-.5 1.2-.6 1.8-.2l2.1 1.6c.6.5.7 1.4.1 2l-1 1c-.9.9-2.3 1.1-3.5.5-3.2-1.5-5.7-4-7.2-7.2-.6-1.2-.4-2.6.5-3.5z" fill="#0b2170"/>
        </svg>
        <span>020 555 0148</span>
      </div>
      <div class="contact-item">
        <svg class="contact-icon" viewBox="0 0 30 30" aria-hidden="true">
          <circle cx="15" cy="15" r="15" fill="#ffffff"/>
          <rect x="8" y="10" width="14" height="10" rx="1.5" fill="none" stroke="#0b2170" stroke-width="1.8"/>
          <path d="M8.5 10.8 15 15.6l6.5-4.8" fill="none" stroke="#0b2170" stroke-width="1.8"/>
        </svg>
        <span>join@circlemetal.co.nz</span>
      </div>
    </footer>
  </main>
</body>
</html>
```